Info Graphic for our IT Staff Augmentation Page

Our offering would be:
-Programmers
-Project Managers
-Testers
-Solutions Architects
-Designers
-Applications Adminstrators
-Network Administrators
-PC/Help Desk Support

We would offer: Onsite | Offsite | Remote

Please see our Website for Content Ideas:
http://staging.brovelanetech.example/staff-augmentation/

**** The background video will not stay there in the header. We would be looking to replace with your info graphic. Dimensions should be at least 2000 x 400

Industry/Entity Type

It Support

Requirements
Should not have
• The example info graphic uploaded here is to show the scope of the project. Do not try to simply duplicate...will be rejected and you will waist your time and mine. Please create an interpretation with the service offerings included and look at the existing content in the staff augmentation page to get ideas.

```html
<!DOCTYPE html>
<html lang="en">
<head>
<meta charset="utf-8">
<title>Custom Software Design for Your Business</title>
<link rel="stylesheet" href="https://fonts.googleapis.com/css2?family=Michroma&family=Open+Sans:wght@600&display=swap">
<style>
  :root {
    --sky-top: #e9eef2;
    --sky-mid: #d3dde4;
    --sky-low: #e4e8ec;
    --blob-violet: #b6b3cc;
    --blob-sage: #cfd6b8;
    --blob-rose: #e6dde9;
    --blob-mist: #dfe5df;
    --accent-orange: #f0c38a;
    --accent-green: #c6dcae;
    --accent-blue: #b9d2e6;
    --bubble-light: #ffffff;
    --bubble-dark: #d6d8da;
    --ink: #1e1f22;
    --call-red: #c4161c;
    --team-light: #f6f7f8;
    --team-dark: #c9ccd0;
  }
  html, body {
    margin: 0;
    padding: 0;
    overflow: hidden;
  }
  .banner {
    position: relative;
    width: 1200px;
    height: 240px;
    overflow: hidden;
    background: linear-gradient(180deg, var(--sky-top) 0%, var(--sky-mid) 55%, var(--sky-low) 100%);
    font-family: "Open Sans", Arial, sans-serif;
  }
  .backdrop {
    position: absolute;
    inset: 0;
  }
  .headline,
  .call-to-action {
    position: absolute;
    left: 0;
    width: 1200px;
    margin: 0;
    text-align: center;
    font-family: "Michroma", "Arial Black", sans-serif;
    font-weight: 400;
    text-transform: uppercase;
  }
  .headline {
    top: 14px;
    font-size: 11.5px;
    letter-spacing: 3.6px;
    color: var(--ink);
  }
  .call-to-action {
    top: 217px;
    font-size: 8.5px;
    letter-spacing: 2.4px;
    color: var(--call-red);
  }
  .team-figure {
    position: absolute;
    left: 436px;
    top: 40px;
    width: 300px;
    height: 172px;
    border-radius: 40px 40px 10px 10px;
    background: radial-gradient(ellipse at 50% 40%, var(--team-light) 0%, #e3e5e8 55%, var(--team-dark) 100%);
    opacity: 0.9;
  }
  .role-bubble {
    position: absolute;
    display: flex;
    align-items: center;
    justify-content: center;
    text-align: center;
    box-sizing: border-box;
    padding: 0 8px;
    font-size: 10px;
    font-weight: 600;
    line-height: 1.3;
    color: var(--ink);
    filter: drop-shadow(1px 3px 3px rgba(60, 70, 80, 0.35));
  }
  .role-bubble::before {
    content: "";
    position: absolute;
    inset: 0;
    border-radius: 50%;
    background: radial-gradient(ellipse at 40% 30%, var(--bubble-light) 30%, var(--bubble-dark) 100%);
    z-index: -1;
  }
  .role-bubble::after {
    content: "";
    position: absolute;
    bottom: -9px;
    width: 20px;
    height: 16px;
    background: var(--bubble-dark);
    z-index: -1;
  }
  .role-bubble span { position: relative; }
  .tail-right::after {
    right: 24%;
    clip-path: polygon(0 0, 60% 0, 100% 100%);
  }
  .tail-left::after {
    left: 24%;
    clip-path: polygon(40% 0, 100% 0, 0 100%);
  }
  .testers      { left: 232px; top: 25px;  width: 68px;  height: 46px; }
  .managers     { left: 137px; top: 59px;  width: 108px; height: 70px; }
  .programmers  { left: 294px; top: 99px;  width: 92px;  height: 62px; }
  .architects   { left: 199px; top: 159px; width: 86px;  height: 58px; }
  .designers    { left: 902px; top: 26px;  width: 80px;  height: 48px; }
  .app-admins   { left: 989px; top: 44px;  width: 106px; height: 72px; }
  .helpdesk     { left: 821px; top: 90px;  width: 90px;  height: 64px; }
  .network      { left: 931px; top: 141px; width: 100px; height: 68px; }
</style>
</head>
<body>
<div class="banner">
  <svg class="backdrop" width="1200" height="240" viewBox="0 0 1200 240" aria-hidden="true">
    <defs>
      <filter id="soften" x="-20%" y="-20%" width="140%" height="140%">
        <feGaussianBlur stdDeviation="4"/>
      </filter>
    </defs>
    <g filter="url(#soften)" opacity="0.85">
      <ellipse cx="-10" cy="150" rx="140" ry="150" fill="var(--blob-violet)"/>
      <ellipse cx="60" cy="15" rx="110" ry="40" fill="var(--blob-sage)" opacity="0.6"/>
      <ellipse cx="260" cy="120" rx="170" ry="70" transform="rotate(18 260 120)" fill="var(--blob-sage)" opacity="0.75"/>
      <ellipse cx="900" cy="60" rx="140" ry="50" fill="var(--blob-mist)"/>
      <ellipse cx="1060" cy="150" rx="200" ry="120" fill="var(--blob-rose)"/>
      <ellipse cx="1160" cy="60" rx="80" ry="90" fill="var(--blob-violet)" opacity="0.55"/>
      <path d="M1100 0 C1140 20 1190 25 1200 60 L1200 0 Z" fill="var(--accent-orange)" opacity="0.7"/>
      <path d="M1120 30 C1150 45 1180 40 1200 70 L1200 40 C1180 25 1150 22 1120 30 Z" fill="var(--accent-green)"/>
      <path d="M1060 8 C1100 28 1130 18 1160 0 L1090 0 Z" fill="var(--accent-blue)" opacity="0.8"/>
    </g>
  </svg>

  <h1 class="headline">Custom Software Design for Your Business</h1>

  <div class="team-figure" role="img" aria-label="Illustration of a team of five IT staff figures standing together with arrows pointing outward"></div>

  <div class="role-bubble tail-right testers"><span>Testers</span></div>
  <div class="role-bubble tail-right managers"><span>Project Managers</span></div>
  <div class="role-bubble tail-left programmers"><span>Programmers</span></div>
  <div class="role-bubble tail-right architects"><span>Solutions<br>Architects</span></div>

  <div class="role-bubble tail-left designers"><span>Designers</span></div>
  <div class="role-bubble tail-right app-admins"><span>Applications<br>Adminstrators</span></div>
  <div class="role-bubble tail-left helpdesk"><span>PC/Help Desk<br>Support</span></div>
  <div class="role-bubble tail-right network"><span>Network<br>Administrators</span></div>

  <p class="call-to-action">Call today for a free brainstorming session!</p>
</div>
</body>
</html>
```